Quimby's Yard & Garden Center Business Card Update

I need an updated Business card design for my Lawn and Garden Center. We do Landscaping installs, Lawn Mowing, Snow Removal and also have a Garden Center Retail Division. I uploaded a few of our previous business cards to give an idea of what we are starting with. The main goal of this update is to simplify and modernize the business card, not all of the services that are on the previous cards has to be on the new one but I would still like to highlight our main services. There is also a sample of our logo that Can be used in the design.

Industry/Entity Type

Landscaping

Contact Information for Business Card

Morris Quimby
Morris@Quimbysyardandgarden.example
Business (555) 201-7784
Cell (555) 318-6092

Colors

Designer to choose colors to be used in the design.

Requirements
Must have
• Services Provided :
• Landscaping
• Lawn Maintenance
• Snow Removal
• Garden Center

```html
<!DOCTYPE html>
<html lang="en">
<head>
<meta charset="utf-8">
<title>Quimby's Yard &amp; Garden Center — Business Card</title>
<link href="https://fonts.googleapis.com/css2?family=Jost:wght@600;700&family=Oswald:wght@500&display=swap" rel="stylesheet">
<style>
  :root {
    --green: #336633;
    --ink: #111111;
    --paper: #ffffff;
    --edge: #333333;
    --shadow: rgba(0, 0, 0, 0.22);
  }
  html, body {
    margin: 0;
    padding: 0;
    width: 1200px;
    height: 1198px;
    overflow: hidden;
    background: var(--paper);
  }
  .stage {
    position: relative;
    width: 1200px;
    height: 1198px;
  }
  .card {
    position: absolute;
    width: 505px;
    height: 288px;
    background: var(--paper);
    border: 1px solid var(--edge);
    box-sizing: border-box;
    box-shadow: 4px 5px 8px var(--shadow);
  }
  .card--back {
    left: 458px;
    top: 577px;
    z-index: 1;
  }
  .card--front {
    left: 227px;
    top: 321px;
    z-index: 2;
    overflow: hidden;
  }
  .brand {
    position: absolute;
    left: 0;
    right: 0;
    top: 0;
    height: 216px;
    display: flex;
    align-items: center;
    justify-content: center;
    gap: 12px;
  }
  .brand__dot {
    width: 26px;
    height: 26px;
    border-radius: 50%;
    background: var(--green);
    flex: none;
  }
  .brand__name {
    font-family: 'Jost', sans-serif;
    font-weight: 700;
    font-size: 25px;
    color: var(--ink);
    letter-spacing: 0.01em;
    white-space: nowrap;
  }
  .services {
    position: absolute;
    left: 0;
    right: 0;
    bottom: 0;
    height: 72px;
    background: var(--green);
    display: flex;
    align-items: center;
    justify-content: center;
    gap: 8px;
    font-family: 'Oswald', sans-serif;
    font-weight: 500;
    font-size: 12.5px;
    letter-spacing: 0.1em;
    color: var(--paper);
    text-transform: uppercase;
    white-space: nowrap;
    padding: 0 10px 2px;
    box-sizing: border-box;
  }
  .services__sep {
    width: 4px;
    height: 4px;
    border-radius: 50%;
    background: var(--paper);
    flex: none;
  }
  .contact {
    position: absolute;
    left: 0;
    right: 0;
    margin: 0;
    text-align: center;
    font-family: 'Jost', sans-serif;
    font-weight: 700;
    text-transform: uppercase;
    letter-spacing: 0.07em;
    color: var(--ink);
    white-space: nowrap;
  }
  .contact--name { top: 60px; font-size: 16.5px; color: var(--green); }
  .contact--email { top: 85px; font-size: 15.5px; letter-spacing: 0.06em; }
  .contact--phones { top: 123px; font-size: 16.5px; line-height: 19px; }
  .contact--address { top: 240px; font-size: 16.5px; letter-spacing: 0.09em; }
</style>
</head>
<body>
  <main class="stage">
    <section class="card card--back" aria-label="Business card back">
      <p class="contact contact--name">Morris Quimby</p>
      <p class="contact contact--email">Morris@Quimbysyardandgarden.example</p>
      <p class="contact contact--phones">P (555) 201-7784<br>C (555) 318-6092</p>
      <p class="contact contact--address">1420 County Road K Maplewood, OH 45999</p>
    </section>

    <section class="card card--front" aria-label="Business card front">
      <div class="brand">
        <span class="brand__dot" aria-hidden="true"></span>
        <span class="brand__name">Quimby's Yard &amp; Garden Center</span>
      </div>
      <div class="services">
        <span>Landscaping</span>
        <span class="services__sep" aria-hidden="true"></span>
        <span>Lawn Maintenance</span>
        <span class="services__sep" aria-hidden="true"></span>
        <span>Snow Removal</span>
        <span class="services__sep" aria-hidden="true"></span>
        <span>Garden Center</span>
      </div>
    </section>
  </main>
</body>
</html>
```